Cover Page for Financial Statements

We need a cover page designed for our Financial Statements. It will need to include our business logo and the Chartered accountant logo.
We have included our current title page ( image titled full.png ) to show all the information that is needed to be included such as the title 'Financial Statements' and 'The year ended March 2023'. We would like to see designs that reflect our logo but also adds some interest with objects / deisngs that fill up more of the page.

Industry/Entity Type

Accounting

Font styles to use
Serif
Sans Serif

Colors

Designer to choose only greyscale colors for use in the design.

Requirements
Must have
• - A4 document size, our logo, Chartered Accountant Logo
Should not have
• Bright Colors

```html
<!DOCTYPE html>
<html lang="en">
<head>
<meta charset="utf-8">
<title>Financial Statements Cover — Year Ended March 2023</title>
<link href="https://fonts.googleapis.com/css2?family=Roboto:wght@400;500;700&display=swap" rel="stylesheet">
<style>
  :root {
    --backdrop: #f3f3f3;
    --paper: #ffffff;
    --ink: #000000;
    --mid-grey: #6e6e6e;
    --dark-grey: #2a2a2a;
    --reverse: #ffffff;
  }
  html, body {
    margin: 0;
    padding: 0;
    width: 1200px;
    height: 900px;
    overflow: hidden;
    background: var(--backdrop);
    font-family: "Roboto", Arial, sans-serif;
  }
  .cover {
    position: absolute;
    left: 300px;
    top: 33px;
    width: 600px;
    height: 833px;
    background: var(--paper);
    box-shadow: 0 2px 10px rgba(0,0,0,0.08);
    overflow: hidden;
  }
  .cover-header {
    position: absolute;
    left: 0; top: 0;
    width: 600px;
    height: 102px;
    background: var(--paper);
  }
  .cover-body {
    position: absolute;
    left: 0; top: 102px;
    width: 600px;
    height: 731px;
    background: var(--ink);
  }
  .cover-frame {
    position: absolute;
    left: 0; top: 0;
    width: 600px;
    height: 833px;
  }
  .member-mark {
    position: absolute;
    left: 22px;
    top: 28px;
    width: 120px;
    text-align: center;
    color: var(--dark-grey);
  }
  .member-mark__dot {
    display: block;
    width: 30px;
    height: 30px;
    margin: 0 auto 6px;
    border-radius: 50%;
    background: var(--mid-grey);
  }
  .member-mark__name {
    display: block;
    font-size: 6.5px;
    font-weight: 500;
    letter-spacing: 0.3px;
    text-transform: uppercase;
    line-height: 1.3;
  }
  .firm-mark {
    position: absolute;
    left: 418px;
    top: 36px;
    width: 146px;
    color: var(--dark-grey);
    text-transform: uppercase;
  }
  .firm-mark__name {
    display: block;
    font-size: 17px;
    font-weight: 400;
    letter-spacing: 1.6px;
    line-height: 1.1;
  }
  .firm-mark__tagline {
    display: block;
    font-size: 5.5px;
    font-weight: 400;
    letter-spacing: 1.2px;
    text-align: right;
    margin-top: 3px;
  }
  .cover-title {
    position: absolute;
    left: 98px;
    top: 334px;
    margin: 0;
    color: var(--reverse);
    font-size: 64px;
    font-weight: 700;
    letter-spacing: 2.5px;
    line-height: 62px;
    text-transform: uppercase;
  }
  .cover-period {
    position: absolute;
    left: 276px;
    top: 550px;
    color: var(--reverse);
    text-transform: uppercase;
  }
  .cover-period__lead {
    display: block;
    font-size: 25px;
    font-weight: 500;
    letter-spacing: 0.6px;
    line-height: 28px;
  }
  .cover-period__date {
    display: block;
    font-size: 70px;
    font-weight: 700;
    letter-spacing: 2px;
    line-height: 62px;
    margin-top: 4px;
  }
</style>
</head>
<body>
  <main class="cover">
    <div class="cover-header"></div>
    <div class="cover-body"></div>

    <svg class="cover-frame" viewBox="0 0 600 833" aria-hidden="true">
      <g fill="var(--reverse)">
        <!-- heavy corner, top left -->
        <path d="M57 153 H194 V202 H107 V285 H57 Z"/>
        <!-- thin bracket, top right -->
        <rect x="282" y="513" width="0" height="0"/>
        <rect x="282" y="213" width="260" height="6"/>
        <rect x="536" y="213" width="6" height="129"/>
        <!-- thin bracket, lower left -->
        <rect x="57" y="439" width="6" height="186"/>
        <rect x="57" y="619" width="197" height="6"/>
        <!-- divider rule -->
        <rect x="273" y="524" width="265" height="3"/>
        <!-- heavy corner, bottom right -->
        <path d="M550 701 H600 V833 H461 V785 H550 Z"/>
      </g>
    </svg>

    <div class="member-mark">
      <span class="member-mark__dot"></span>
      <span class="member-mark__name">Registered Ledger Professionals</span>
    </div>

    <div class="firm-mark">
      <span class="firm-mark__name">Northgate</span>
      <span class="firm-mark__tagline">Accounting &amp; Advisory</span>
    </div>

    <h1 class="cover-title">Financial<br>Statements</h1>

    <p class="cover-period">
      <span class="cover-period__lead">For the year ended</span>
      <span class="cover-period__date">March<br>2023</span>
    </p>
  </main>
</body>
</html>
```